Profesional personal website needs design and business card

I need a business card with my professional name as a logo "Orlan Vitality" for my business. I am a Wellness Coach, consultant and trainer. So it should be professional, wellness oriented and modern.

Target Market(s)

Private clients, governments, corporations. Luxury and high market.

Industry/Entity Type

Health And Wellness

Contact Information for Business Card

Orlan Vitality should be the logo

Colors

Designer to choose colors to be used in the design.

Requirements
Must have
• Orlan Vitality
• Name: Dario Montalbe
• Wellness Coach, Consultant & Trainer.
• Website: www.orlanvitality-example.com
• Phone:
• Spain (+34) 612 480 597
• (USA) +1 (555) 318 0264
Nice to have
• The most important is the design of "Orlan Vitality", as this is going to be my personal brand logo. It should be professional, wellness, high end and actual.
Should not have
• no golds, no baroque style..

```html
<!DOCTYPE html>
<html lang="en">
<head>
<meta charset="utf-8">
<title>Orlan Vitality — Business Card</title>
<link href="https://fonts.googleapis.com/css2?family=Lato:wght@400;700&display=swap" rel="stylesheet">
<style>
  :root {
    --brand-red: #8e1a1e;
    --ink: #1c1c1c;
    --paper: #ffffff;
    --shadow: rgba(0, 0, 0, 0.32);
  }
  * { margin: 0; padding: 0; box-sizing: border-box; }
  html, body {
    width: 1200px;
    height: 1200px;
    overflow: hidden;
    background: var(--paper);
    font-family: "Lato", sans-serif;
  }
  .canvas { position: relative; width: 1200px; height: 1200px; }

  .card {
    position: absolute;
    left: 180px;
    width: 840px;
    height: 477px;
    box-shadow: 4px 5px 6px var(--shadow);
  }
  .card--front { top: 84px; background: var(--paper); }
  .card--back { top: 640px; background: var(--brand-red); }

  .brand-name {
    position: absolute;
    font-weight: 700;
    white-space: nowrap;
    letter-spacing: 0.5px;
  }
  .card--front .brand-name {
    left: 42px;
    top: 186px;
    width: 304px;
    text-align: center;
    font-size: 40px;
    color: var(--brand-red);
  }
  .card--back .brand-name {
    left: 0;
    width: 840px;
    top: 196px;
    text-align: center;
    font-size: 64px;
    color: var(--paper);
  }

  .accent-tab {
    position: absolute;
    right: 0;
    top: 142px;
    width: 19px;
    height: 190px;
    background: var(--brand-red);
    border-radius: 6px 0 0 6px;
  }

  .contact-block {
    position: absolute;
    right: 44px;
    top: 150px;
    text-align: right;
  }
  .person-name {
    font-weight: 700;
    font-size: 39px;
    line-height: 1;
    color: var(--brand-red);
  }
  .person-role {
    margin-top: 8px;
    font-size: 19px;
    color: var(--ink);
  }
  .contact-list {
    list-style: none;
    margin-top: 22px;
  }
  .contact-item {
    display: flex;
    justify-content: flex-end;
    align-items: center;
    gap: 13px;
    height: 30px;
    font-size: 19px;
    color: var(--ink);
  }
  .contact-item .label { color: var(--brand-red); margin-right: 5px; }
  .contact-icon { width: 18px; height: 18px; fill: var(--brand-red); flex: none; }

  .notch {
    position: absolute;
    top: 141px;
    width: 13px;
    height: 197px;
    background: var(--paper);
  }
  .notch--left { left: 0; border-radius: 0 6px 6px 0; }
  .notch--right { right: 0; border-radius: 6px 0 0 6px; }

  .back-url {
    position: absolute;
    left: 0;
    width: 840px;
    top: 424px;
    text-align: center;
    font-size: 18px;
    color: var(--paper);
  }
</style>
</head>
<body>
<div class="canvas">

  <section class="card card--front">
    <div class="brand-name">Orlan Vitality</div>

    <div class="contact-block">
      <h1 class="person-name">DARIO MONTALBE</h1>
      <p class="person-role">Wellness Coach, Consultant &amp; Trainer</p>
      <ul class="contact-list">
        <li class="contact-item">
          <span><span class="label">Spain</span>(+34) 612 480 597</span>
          <svg class="contact-icon" viewBox="0 0 24 24" aria-hidden="true"><path d="M6.6 10.8a15.1 15.1 0 0 0 6.6 6.6l2.2-2.2a1 1 0 0 1 1-.25 11.4 11.4 0 0 0 3.6.57 1 1 0 0 1 1 1V20a1 1 0 0 1-1 1A17 17 0 0 1 3 4a1 1 0 0 1 1-1h3.5a1 1 0 0 1 1 1c0 1.25.2 2.45.57 3.57a1 1 0 0 1-.25 1z"/></svg>
        </li>
        <li class="contact-item">
          <span><span class="label">(USA)</span>+1 (555) 318 0264</span>
          <svg class="contact-icon" viewBox="0 0 24 24" aria-hidden="true"><path d="M7 1h10a2 2 0 0 1 2 2v18a2 2 0 0 1-2 2H7a2 2 0 0 1-2-2V3a2 2 0 0 1 2-2zm0 3v14h10V4zm5 15.5a1 1 0 1 0 0 2 1 1 0 0 0 0-2z"/></svg>
        </li>
        <li class="contact-item">
          <span>www.orlanvitality-example.com</span>
          <svg class="contact-icon" viewBox="0 0 24 24" aria-hidden="true"><path d="M12 2a10 10 0 1 0 0 20 10 10 0 0 0 0-20zm6.9 6h-2.9a15.6 15.6 0 0 0-1.4-3.6A8 8 0 0 1 18.9 8zM12 4c.8 1.2 1.5 2.5 1.9 4h-3.8c.4-1.5 1.1-2.8 1.9-4zM4.3 14a8.2 8.2 0 0 1 0-4h3.4a16.5 16.5 0 0 0 0 4zm.8 2h2.9c.3 1.3.8 2.5 1.4 3.6A8 8 0 0 1 5.1 16zM8 8H5.1a8 8 0 0 1 4.3-3.6C8.8 5.5 8.4 6.7 8 8zm4 12c-.8-1.2-1.5-2.5-1.9-4h3.8c-.4 1.5-1.1 2.8-1.9 4zm2.3-6H9.7a14.7 14.7 0 0 1 0-4h4.6a14.7 14.7 0 0 1 0 4zm.3 5.6c.6-1.1 1.1-2.3 1.4-3.6h2.9a8 8 0 0 1-4.3 3.6zm1.7-5.6a16.5 16.5 0 0 0 0-4h3.4a8.2 8.2 0 0 1 0 4z"/></svg>
        </li>
      </ul>
    </div>

    <div class="accent-tab"></div>
  </section>

  <section class="card card--back">
    <div class="notch notch--left"></div>
    <div class="notch notch--right"></div>
    <div class="brand-name">Orlan Vitality</div>
    <p class="back-url">www.orlanvitality-example.com</p>
  </section>

</div>
</body>
</html>
```